Small and passionate motorcycle workshop requires a business card that kicks butt!

I'm Dermot, I'm passionate about my motorcycles, I'm passionate about my desert racing and I'm a passionate motorcycle technician, that's why I started my own motorcycle workshop: 'Rivo Tarka'.
I started my workshop in my dining room and it’s eventually moved into a newly renovated shed that my Grandpa built with his own two hands in the early 1960's. To the customer the shed looks like a farm shed on my property, however the inside is ready for open heart surgery on their "Baby" which could be a late model sports bike, a highway cruiser, an old four-wheeler or an off road desert racing weapon!
This business is my own, I've built it from my dining room floor and I'm deeply passionate about it.
I need a professional business card and logo which looks like a heart and soul is intermingled through it because that is how my business is run. Rivo Tarka may have started from my dining room but it has always been professionally run and I have always put my passion into the bikes I've worked on.

-The text only logo needs to be comprised of 'Rivo Tarka'
-The business card will be double sided

And I do realise it will be a hard task to make something look professional and personal at the same time...however there are some very talented people in this world and I can’t wait to see what you create!

I've added some logo/designs that I'm fond of.

Industry/Entity Type

Racing

Requirements
Must have
• My name - Dermot Fasquell
My Qualification - Qualified Motorcycle Technician
Ph - 0487305219
Email - rivotarka@kelpmail.example
Address - 17 Bellwin Ridge Road, Williamstown, SA
ABN - 62 918 304 217 (plesase include the 'ABN' part
Needs to include these dot points:
-Servicing
-Repairs
-All makes/models
-Weekends by appt.
-Pick-up/delivery available
Nice to have
• I like the idea of calling myself a "Qualified and Passionate Motorcycle Technician". If the card does not come across that it’s a passionate business I'd like this line to be used on the card near my name.

One idea I like would include having the text only logo on the front being quite bold and contrasted to the background, then having my name and number smaller underneath somewhere. I'm very open to whatever comes my way so I'm look forward to seeing some sweet ideas!

```html
<!DOCTYPE html>
<html lang="en">
<head>
<meta charset="utf-8">
<title>Rivo Tarka – Business Card</title>
<link rel="stylesheet" href="https://fonts.googleapis.com/css2?family=Didact+Gothic&family=PT+Sans+Narrow:wght@400;700&family=PT+Sans:wght@700&display=swap">
<style>
  :root {
    --ink: #000000;
    --paper: #ffffff;
    --mist: #c4c4c4;
    --mist-light: #dedede;
    --mist-dark: #8a8a8a;
    --signal: #ec1c24;
    --text: #111111;
    --rule: #333333;
  }
  * { margin: 0; padding: 0; box-sizing: border-box; }
  html, body {
    width: 1200px; height: 900px; overflow: hidden;
    background: var(--paper);
  }
  .sheet { position: relative; width: 1200px; height: 900px; }

  .sheet-label {
    position: absolute; left: 36px; top: 44px;
    font: 26px/1 "Didact Gothic", sans-serif; color: var(--text);
  }

  /* Front */
  .card-front {
    position: absolute; left: 41px; top: 98px;
    width: 611px; height: 349px;
    background: var(--ink); overflow: hidden;
  }
  .wordmark {
    position: absolute; left: 6px; top: -10px;
    font: 700 196px/0.9 "PT Sans Narrow", sans-serif;
    color: var(--paper); text-transform: uppercase;
    letter-spacing: -2px;
  }
  .wordmark span { display: block; }
  .owner-name {
    position: absolute; left: 563px; top: 322px;
    transform: rotate(-90deg); transform-origin: left top;
    font: 38px/1 "Didact Gothic", sans-serif;
    color: var(--mist); white-space: nowrap; word-spacing: -6px;
  }

  /* Back */
  .card-back {
    position: absolute; left: 556px; top: 478px;
    width: 611px; height: 350px;
    background: var(--paper); border: 1px solid var(--rule);
  }
  .qual-band {
    position: absolute; left: 652px; top: 470px;
    width: 135px; height: 285px; background: var(--ink);
  }
  .splash {
    position: absolute; left: 600px; top: 556px;
    width: 460px; height: 46px; border-radius: 24px 30px 18px 24px;
    background: linear-gradient(90deg, var(--mist-light) 0%, var(--mist-dark) 30%, var(--mist) 55%, var(--mist-light) 100%);
    opacity: 0.75;
  }
  .qualification {
    position: absolute; left: 652px; top: 646px; width: 135px;
    text-align: center; color: var(--paper);
    font: 700 26px/35px "PT Sans Narrow", sans-serif; letter-spacing: -0.4px;
  }
  .services {
    position: absolute; right: 76px; top: 502px;
    list-style: none; text-align: right;
    font: 400 20px/26.2px "PT Sans Narrow", sans-serif; color: var(--text);
  }
  .phone {
    position: absolute; right: 76px; top: 678px;
    font: 700 36px/1 "PT Sans", sans-serif; color: var(--signal);
  }
  .contact-line {
    position: absolute; right: 77px; top: 787px;
    font: 400 16px/1 "PT Sans Narrow", sans-serif; color: var(--text);
    white-space: nowrap;
  }
  .contact-line .sep { color: var(--signal); margin: 0 3px; }
</style>
</head>
<body>
<main class="sheet">
  <p class="sheet-label">Front of business card</p>

  <section class="card-front" aria-label="Business card front">
    <h1 class="wordmark"><span>Rivo</span><span>Tarka</span></h1>
    <p class="owner-name">Dermot Fasquell</p>
  </section>

  <section class="card-back" aria-label="Business card back"></section>
  <div class="qual-band"></div>
  <div class="splash" role="img" aria-label="Grey brush-stroke splash across the card"></div>
  <p class="qualification">Qualified<br>Motorcycle<br>Technician</p>
  <ul class="services">
    <li>Servicing</li>
    <li>Repairs</li>
    <li>All makes &amp; models</li>
    <li>Weekends by appointment</li>
    <li>Pick-up &amp; delivery available</li>
  </ul>
  <p class="phone">Ph 0487305219</p>
  <p class="contact-line">17 Bellwin Ridge Road<span class="sep">|</span>Williamstown, SA<span class="sep">|</span>ABN 62 918 304 217<span class="sep">|</span>rivotarka@kelpmail.example</p>
</main>
</body>
</html>
```